Adventurous female pilot

I am looking for a personal business card, for a very well qualified female pilot, with a lot of aviation experience.

Currently an airline pilot, have worked as a bush pilot in Africa, looking to get into corporate aviation, or private jet owners.
Want a classy looking card for networking...

Could be interested in a retro\vintage look also?!

An idea,, is an african sunset background, with my wings\logo on it
Updates

I just want to say thank you to all of your for your amazing designs!

I have been very busy flying this past week , so not had a chance to be on the computer much.
But I provide some feedback, and conclusions very soon!
Thank you again.

Marla

Reason: Still waiting on a couple of revisions to be 100% about my choice!

Target Market(s)

corporate aviation, private jet owners, casino's,
General audience.
networking

Industry/Entity Type

Airline

Requirements
Nice to have
• Classy, edgy, sexy, but also feminine

```html
<!DOCTYPE html>
<html lang="en">
<head>
<meta charset="utf-8">
<title>Marla Hale – Airline Pilot</title>
<link href="https://fonts.googleapis.com/css2?family=Advent+Pro:wght@500;600&display=swap" rel="stylesheet">
<style>
  :root {
    --card-gold: #ffb22e;
    --ink-maroon: #5a0a06;
    --ink-amber: #b0601a;
  }
  html, body {
    margin: 0;
    padding: 0;
    overflow: hidden;
    background: var(--card-gold);
  }
  .card {
    position: relative;
    width: 686px;
    height: 1200px;
    background: var(--card-gold);
    font-family: "Advent Pro", sans-serif;
    color: var(--ink-maroon);
    overflow: hidden;
  }
  .brand-mark {
    position: absolute;
    top: 290px;
    left: 0;
    width: 686px;
    display: flex;
    justify-content: center;
    align-items: center;
    gap: 16px;
  }
  .brand-mark__dot {
    width: 56px;
    height: 56px;
    border-radius: 50%;
    background: var(--ink-maroon);
  }
  .brand-mark__name {
    font-size: 44px;
    font-weight: 600;
    letter-spacing: 2px;
    text-transform: uppercase;
    color: var(--ink-maroon);
  }
  .identity {
    position: absolute;
    top: 496px;
    left: 0;
    width: 686px;
    text-align: center;
  }
  .identity__name {
    margin: 0;
    font-size: 56px;
    font-weight: 600;
    letter-spacing: 1px;
    text-transform: uppercase;
    line-height: 1;
  }
  .identity__role {
    margin: 14px 0 0;
    font-size: 27px;
    font-weight: 500;
    letter-spacing: 1px;
    text-transform: uppercase;
    color: var(--ink-amber);
    line-height: 1;
  }
  .contacts {
    position: absolute;
    top: 628px;
    left: 0;
    width: 686px;
    margin: 0;
    padding: 0;
    list-style: none;
    text-align: center;
  }
  .contacts__item {
    font-size: 38px;
    font-weight: 600;
    line-height: 1;
    height: 58px;
    text-transform: uppercase;
    letter-spacing: 0.5px;
  }
  .contacts__label {
    color: var(--ink-amber);
    font-weight: 500;
    text-decoration: underline;
    text-decoration-thickness: 3px;
    text-underline-offset: 6px;
    margin-right: 10px;
  }
  .rule-stack {
    position: absolute;
    top: 850px;
    left: 0;
  }
</style>
</head>
<body>
  <div class="card">
    <div class="brand-mark">
      <span class="brand-mark__dot"></span>
      <span class="brand-mark__name">Hale Wings</span>
    </div>

    <header class="identity">
      <h1 class="identity__name">Marla Hale</h1>
      <p class="identity__role">Airline Pilot</p>
    </header>

    <ul class="contacts">
      <li class="contacts__item"><span class="contacts__label">Email</span> marlachale@skymail.net</li>
      <li class="contacts__item"><span class="contacts__label">Cell</span>702.555.0148</li>
      <li class="contacts__item"><span class="contacts__label">Taipei Cell</span>886.900.555.214</li>
    </ul>

    <svg class="rule-stack" width="686" height="120" viewBox="0 0 686 120" aria-hidden="true">
      <rect x="215" y="4" width="256" height="8" fill="var(--ink-maroon)"/>
      <rect x="250" y="52" width="186" height="8" fill="var(--ink-maroon)"/>
      <rect x="303" y="99" width="79" height="8" fill="var(--ink-maroon)"/>
    </svg>
  </div>
</body>
</html>
```